Calloway Ridge Associates Stationery

Use attached logo for stationery
Stationery, Letterhead and Envelope + Business cards

Tag line: Walking alongside those doing the work of the Gospel

```html
<!DOCTYPE html>
<html lang="en">
<head>
<meta charset="utf-8">
<title>Calloway Ridge Associates – Business Card</title>
<link href="https://fonts.googleapis.com/css2?family=Roboto:wght@400;700&display=swap" rel="stylesheet">
<style>
  :root {
    --page-bg: #2a2a2c;
    --card-white: #f7f7f8;
    --card-dark: #1d1d1f;
    --brand-blue: #1f5fa8;
    --brand-navy: #0f4380;
    --brand-sky: #5aaed0;
    --brand-gold: #e2a21a;
    --text-grey: #555a60;
    --rule-grey: #b9bcc0;
  }
  * { box-sizing: border-box; margin: 0; padding: 0; }
  html, body { width: 1200px; height: 1200px; overflow: hidden; }
  body {
    background: var(--page-bg);
    font-family: "Roboto", sans-serif;
    display: flex;
    flex-direction: column;
    align-items: center;
    justify-content: center;
    gap: 70px;
  }
  .card {
    width: 840px;
    height: 480px;
    border-radius: 4px;
    box-shadow: 0 18px 40px rgba(0,0,0,0.45);
    position: relative;
  }
  .card-front {
    background: var(--card-white);
    display: flex;
    align-items: center;
    padding: 0 60px;
  }
  .brand-block {
    flex: 0 0 330px;
    display: flex;
    align-items: center;
    gap: 14px;
  }
  .brand-dot {
    width: 22px; height: 22px;
    border-radius: 50%;
    background: var(--brand-gold);
    flex: none;
  }
  .brand-name {
    font-weight: 700;
    font-size: 30px;
    line-height: 1.15;
    color: var(--brand-blue);
    letter-spacing: 0.5px;
  }
  .divider {
    width: 1px;
    height: 250px;
    background: var(--rule-grey);
    margin: 0 44px 0 30px;
  }
  .contact-block { color: var(--text-grey); }
  .person-name {
    font-weight: 700;
    font-size: 34px;
    color: var(--brand-blue);
  }
  .person-title {
    font-size: 18px;
    margin-top: 4px;
  }
  .address {
    font-size: 18px;
    line-height: 1.45;
    margin-top: 22px;
  }
  .contact-list {
    list-style: none;
    margin-top: 14px;
    font-size: 18px;
    line-height: 1.55;
  }
  .contact-list li { display: flex; align-items: center; gap: 10px; }
  .contact-list svg { width: 16px; height: 16px; flex: none; }
  .card-back {
    background: var(--card-dark);
    display: flex;
    align-items: center;
    justify-content: center;
    gap: 18px;
  }
  .card-back .brand-name { font-size: 44px; }
  .card-back .brand-dot { width: 30px; height: 30px; }
</style>
</head>
<body>
  <section class="card card-front">
    <div class="brand-block">
      <span class="brand-dot"></span>
      <span class="brand-name">Calloway Ridge Associates</span>
    </div>
    <div class="divider"></div>
    <div class="contact-block">
      <h1 class="person-name">Daniel Harper</h1>
      <p class="person-title">Managing Director</p>
      <p class="address">48 Orchard Crest Lane<br>Fairview, SC 29311</p>
      <ul class="contact-list">
        <li>
          <svg viewBox="0 0 16 16" aria-hidden="true"><path d="M4 1l3 3-2 2c1 2 3 4 5 5l2-2 3 3-2 3C7 15 1 9 1 3z" fill="#1f5fa8"/></svg>
          (555) 014-2273
        </li>
        <li>
          <svg viewBox="0 0 16 16" aria-hidden="true"><rect x="1" y="3" width="14" height="10" rx="1" fill="#1f5fa8"/><path d="M1 4l7 5 7-5" stroke="#fff" stroke-width="1.4" fill="none"/></svg>
          info@callowayridge.org
        </li>
        <li>
          <svg viewBox="0 0 16 16" aria-hidden="true"><circle cx="8" cy="8" r="6.5" fill="none" stroke="#1f5fa8" stroke-width="1.4"/><ellipse cx="8" cy="8" rx="2.8" ry="6.5" fill="none" stroke="#1f5fa8" stroke-width="1.2"/><path d="M1.5 8h13M2.5 5h11M2.5 11h11" stroke="#1f5fa8" stroke-width="1.1"/></svg>
          www.callowayridge.org
        </li>
      </ul>
    </div>
  </section>

  <section class="card card-back">
    <span class="brand-dot"></span>
    <span class="brand-name">Calloway Ridge Associates</span>
  </section>
</body>
</html>
```